wealth management firm, professional group, new model

we have a logo that works but we need a card, white background using our colors...clean look

our tag line if can be used in

Where Every Client Builds Lasting Value

```html
<!DOCTYPE html>
<html lang="en">
<head>
<meta charset="utf-8">
<title>Arcora Capital Advisors – Business Card</title>
<link rel="stylesheet" href="https://fonts.googleapis.com/css2?family=Lato:wght@300;400;700&display=swap">
<style>
  :root {
    --backdrop: #8499bb;
    --navy: #1f3358;
    --navy-deep: #1a2c4e;
    --ink: #2c3e63;
    --ink-soft: #5a6a88;
    --paper: #ffffff;
    --rule: #9aa6bd;
  }
  * { box-sizing: border-box; margin: 0; padding: 0; }
  html, body {
    width: 1200px;
    height: 876px;
    overflow: hidden;
  }
  body {
    background: var(--backdrop);
    font-family: "Lato", sans-serif;
    display: flex;
    align-items: center;
    justify-content: center;
    gap: 60px;
  }
  .card {
    width: 500px;
    height: 286px;
    border-radius: 22px;
    position: relative;
    box-shadow: 0 14px 30px rgba(30, 45, 80, 0.25);
  }

  /* Front: contact side */
  .card--front {
    background: var(--paper);
    display: flex;
    align-items: center;
    padding-left: 40px;
  }
  .identity {
    text-align: right;
    padding-right: 16px;
  }
  .identity__name {
    font-weight: 700;
    font-size: 15px;
    color: var(--ink);
    letter-spacing: 0.02em;
  }
  .identity__role {
    font-weight: 400;
    font-size: 12px;
    color: var(--ink-soft);
    margin-top: 3px;
  }
  .divider {
    width: 1px;
    height: 68px;
    background: var(--rule);
    align-self: center;
    margin-top: 60px;
  }
  .contact {
    list-style: none;
    padding-left: 12px;
    margin-top: 66px;
  }
  .contact__item {
    display: flex;
    align-items: center;
    gap: 6px;
    font-size: 15px;
    color: var(--ink);
    line-height: 1.35;
  }
  .contact__icon { width: 12px; height: 12px; flex: none; }

  /* Back: brand side */
  .card--back {
    background: linear-gradient(160deg, #26406b 0%, var(--navy) 45%, var(--navy-deep) 100%);
    color: var(--paper);
    display: flex;
    flex-direction: column;
    align-items: center;
    justify-content: center;
    text-align: center;
  }
  .brand__name {
    font-weight: 300;
    font-size: 42px;
    letter-spacing: 0.42em;
    margin-right: -0.42em;
    line-height: 1;
    color: var(--paper);
  }
  .brand__descriptor {
    font-weight: 300;
    font-size: 15px;
    letter-spacing: 0.18em;
    margin-right: -0.18em;
    margin-top: 10px;
    color: var(--paper);
  }
  .tagline {
    font-weight: 300;
    font-size: 12px;
    letter-spacing: 0.28em;
    margin-right: -0.28em;
    text-transform: uppercase;
    margin-top: 34px;
    color: var(--paper);
  }
</style>
</head>
<body>

  <section class="card card--front" aria-label="Card front">
    <div class="identity">
      <p class="identity__name">DANIEL HART</p>
      <p class="identity__role">Director</p>
    </div>
    <span class="divider"></span>
    <ul class="contact">
      <li class="contact__item">
        <svg class="contact__icon" viewBox="0 0 12 12" aria-hidden="true">
          <circle cx="6" cy="6" r="6" fill="#2c3e63"/>
          <rect x="3" y="4" width="6" height="4.2" fill="none" stroke="#fff" stroke-width="0.9"/>
          <path d="M3 4 L6 6.4 L9 4" fill="none" stroke="#fff" stroke-width="0.9"/>
        </svg>
        hello@arcoracapital.co
      </li>
      <li class="contact__item">
        <svg class="contact__icon" viewBox="0 0 12 12" aria-hidden="true">
          <circle cx="6" cy="6" r="6" fill="#2c3e63"/>
          <path d="M4.2 3.2 L5.2 4.6 L4.6 5.3 Q5.4 6.8 6.8 7.4 L7.5 6.8 L8.8 7.8 L8.2 8.8 Q5 8.6 3.4 4.2 Z" fill="#fff"/>
        </svg>
        014 555 0182
      </li>
    </ul>
  </section>

  <section class="card card--back" aria-label="Card back">
    <p class="brand__name">ARCORA</p>
    <p class="brand__descriptor">CAPITAL ADVISORS</p>
    <p class="tagline">Where Every Client Builds Lasting Value</p>
  </section>

</body>
</html>
```